We sell companies excess stock for them

We need a business card for a company based in New Zealand called 'StockHarbor'.

Check out our website to get an idea www.stockharbor.example

We help other businesses to;
- Sell Excess Stock
- Manage Product Returns
- Sell Company Assets

Our logo is attached for your reference
The font used is 'RifficFree-Bold'

Target Market(s)

Businesses

Industry/Entity Type

Business

Contact Information for Business Card

Name: Mark Pellow
Phone: 027 846 2093
email: markpellow@stockharbor.example
website: www.stockharbor.example

Font styles to use
Other font styles liked:
• Unsure

Colors
9bcb3b

Requirements
Must have
• coming soon
Nice to have
• coming soon
Should not have
• coming soon

```html
<!DOCTYPE html>
<html lang="en">
<head>
<meta charset="utf-8">
<title>StockHarbor — Business Card</title>
<link rel="stylesheet" href="https://fonts.googleapis.com/css2?family=Mr+Dafoe&family=Montserrat:wght@400&display=swap">
<style>
  :root {
    --brand-green: #9bcb3b;
    --ink: #2b2b2d;
    --card: #fbfbfa;
    --backdrop: #e6e5e2;
    --photo-light: #f4f4f2;
    --photo-mid: #e9e9e6;
  }
  * { box-sizing: border-box; margin: 0; padding: 0; }
  html, body {
    width: 1200px; height: 1200px; overflow: hidden;
    background: var(--backdrop);
  }
  .canvas {
    position: relative; width: 1200px; height: 1200px;
    display: flex; align-items: center; justify-content: center;
  }
  .business-card {
    position: relative; width: 1000px; height: 572px;
    background: var(--card);
    box-shadow: 0 18px 40px rgba(0,0,0,0.12);
    overflow: hidden;
  }
  .card-photo {
    position: absolute; inset: 0;
    background: linear-gradient(180deg, var(--card) 0%, var(--photo-light) 55%, var(--photo-mid) 100%);
  }
  .card-content {
    position: absolute; inset: 0;
    display: flex; flex-direction: column; align-items: center;
    padding-top: 180px;
  }
  .holder-name {
    font-family: "Mr Dafoe", cursive;
    font-size: 104px; line-height: 1;
    white-space: nowrap;
    margin-left: 120px;
  }
  .holder-name .first { color: var(--brand-green); }
  .holder-name .last { color: var(--ink); position: relative; top: 34px; margin-left: 14px; }
  .contact-list {
    margin-top: 22px;
    font-family: "Montserrat", sans-serif;
    font-size: 30px; color: var(--ink);
    display: flex; flex-direction: column; align-items: center; gap: 12px;
  }
  .contact-row { display: flex; align-items: center; gap: 26px; }
  .contact-item { display: flex; align-items: center; gap: 12px; white-space: nowrap; }
  .contact-icon { width: 34px; height: 34px; flex: none; }
</style>
</head>
<body>
<main class="canvas">
  <section class="business-card">
    <div class="card-photo" role="img" aria-label="Faint office interior photograph behind the card text"></div>
    <div class="card-content">
      <h1 class="holder-name"><span class="first">Mark</span><span class="last">Pellow</span></h1>
      <div class="contact-list">
        <div class="contact-row">
          <span class="contact-item">
            <svg class="contact-icon" viewBox="0 0 34 34" aria-hidden="true">
              <circle cx="17" cy="17" r="17" fill="var(--brand-green)"/>
              <rect x="12" y="8" width="10" height="18" rx="2" fill="none" stroke="#fff" stroke-width="2"/>
              <line x1="15" y1="22.5" x2="19" y2="22.5" stroke="#fff" stroke-width="1.6"/>
            </svg>
            027-846-2093
          </span>
          <span class="contact-item">
            <svg class="contact-icon" viewBox="0 0 34 34" aria-hidden="true">
              <circle cx="17" cy="17" r="17" fill="var(--brand-green)"/>
              <g fill="none" stroke="#fff" stroke-width="1.8">
                <circle cx="17" cy="17" r="9"/>
                <ellipse cx="17" cy="17" rx="4" ry="9"/>
                <line x1="8" y1="17" x2="26" y2="17"/>
                <line x1="10" y1="12" x2="24" y2="12"/>
                <line x1="10" y1="22" x2="24" y2="22"/>
              </g>
            </svg>
            www.stockharbor.example
          </span>
        </div>
        <div class="contact-row">
          <span class="contact-item">
            <svg class="contact-icon" viewBox="0 0 34 34" aria-hidden="true">
              <circle cx="17" cy="17" r="17" fill="var(--brand-green)"/>
              <rect x="9" y="11" width="16" height="12" rx="1" fill="#fff"/>
              <polyline points="9,11 17,18 25,11" fill="none" stroke="var(--brand-green)" stroke-width="1.8"/>
            </svg>
            markpellow@stockharbor.example
          </span>
        </div>
      </div>
    </div>
  </section>
</main>
</body>
</html>
```